Buchungsplattform für Hypnose-Dienstleistungen sucht Zertifikat-Design
Zielgruppe
Buchungsplattform für Hypnose Dienstleistungen. Die Zielgruppe des angeklagten Design (Zertifikat) geht an registrierte Anbieter (Hypnosetherapeuten, Praxes, Zahnärzte, etc).
Aufgabenstellung
Das gewünschte Zertifikat soll;
- unser CI/CD berücksichtigen (Primär Orange: #DD3200 Sekundär Blau: #0085A8(
- soll einen wertvollen, aufwendigen, besonderen Eindruck vermitteln
- soll sich inhaltlich in etwa dem angehängten Vorschlag orientieren
- kann spezielle Druckverfahren (Prägedruck, Stanz, Laser, etc. ) in Erwägung ziehen wo angebracht

```html
<!DOCTYPE html>
<html lang="de">
<head>
<meta charset="utf-8">
<title>Certificate of Excellence – Somnaris</title>
<link rel="stylesheet" href="https://fonts.googleapis.com/css2?family=EB+Garamond:wght@400;600&family=Montserrat:wght@400&display=swap">
<style>
  :root {
    --accent: #e8501e;
    --ink: #111111;
    --paper: #ffffff;
    --sand-light: #f5f0e7;
    --sand-dark: #e9e0cd;
    --gold-light: #efdb6e;
    --gold-mid: #d9bf45;
    --gold-dark: #bfa032;
    --frame: #9a9a9a;
  }
  html, body {
    margin: 0;
    padding: 0;
    overflow: hidden;
    background: var(--paper);
  }
  .certificate {
    position: relative;
    width: 848px;
    height: 1200px;
    background: var(--paper);
    box-sizing: border-box;
    border: 1px solid var(--frame);
    overflow: hidden;
    font-family: "EB Garamond", Garamond, serif;
    color: var(--ink);
  }
  .backdrop, .ribbon-seal {
    position: absolute;
    inset: 0;
    width: 848px;
    height: 1200px;
  }
  .brand {
    position: absolute;
    left: 291px;
    top: 132px;
    margin: 0;
    font-family: "Montserrat", Arial, sans-serif;
    font-weight: 400;
    font-size: 64px;
    letter-spacing: 1px;
    color: var(--accent);
    line-height: 1;
  }
  .title {
    position: absolute;
    left: 0;
    right: 0;
    top: 372px;
    margin: 0;
    text-align: center;
    font-weight: 600;
    font-size: 69px;
    line-height: 75px;
    color: var(--accent);
    letter-spacing: 1px;
  }
  .practice-name {
    position: absolute;
    left: 0;
    right: 0;
    top: 540px;
    margin: 0;
    text-align: center;
    font-weight: 400;
    font-size: 70px;
    line-height: 70px;
  }
  .rule {
    position: absolute;
    height: 2px;
    background: linear-gradient(to right, transparent, var(--accent) 15%, var(--accent) 85%, transparent);
  }
  .rule--name { left: 174px; width: 500px; top: 623px; }
  .rule--sign { left: 263px; width: 318px; top: 970px; }
  .holder {
    position: absolute;
    left: 0;
    right: 0;
    top: 640px;
    margin: 0;
    text-align: center;
    font-size: 21.5px;
    line-height: 29px;
    text-transform: uppercase;
    letter-spacing: 0.3px;
  }
  .citation {
    position: absolute;
    left: 0;
    right: 0;
    top: 715px;
    margin: 0;
    text-align: center;
    font-size: 42px;
    line-height: 47px;
  }
  .issuer {
    position: absolute;
    left: 301px;
    top: 979px;
    margin: 0;
    font-size: 23px;
    line-height: 30px;
    text-transform: uppercase;
    letter-spacing: 0.3px;
  }
</style>
</head>
<body>
<main class="certificate">
  <svg class="backdrop" viewBox="0 0 848 1200" aria-hidden="true">
    <polygon points="848,728 848,1200 45,1200" fill="var(--sand-light)"/>
    <polygon points="0,863 335,1200 0,1200" fill="var(--sand-dark)" opacity="0.85"/>
  </svg>

  <svg class="ribbon-seal" viewBox="0 0 848 1200">
    <defs>
      <linearGradient id="gold" x1="0" y1="0" x2="1" y2="1">
        <stop offset="0" stop-color="var(--gold-light)"/>
        <stop offset="1" stop-color="var(--gold-dark)"/>
      </linearGradient>
    </defs>
    <polygon class="ribbon" points="258,0 321,0 0,332 0,260" fill="url(#gold)"/>
    <circle class="seal" cx="142" cy="155" r="104" fill="url(#gold)" role="img" aria-label="Platz für goldenes Gütesiegel"/>
  </svg>

  <p class="brand">SOMNARIS</p>

  <h1 class="title">CERTIFICATE<br>OF EXELLENCE</h1>

  <h2 class="practice-name">Praxisname</h2>
  <div class="rule rule--name"></div>

  <p class="holder">Vorname&nbsp; Nachname<br>Adresse &nbsp; / &nbsp;&nbsp; PLZ Ort</p>

  <p class="citation">wird für seine hervorragende Qualität<br>und Betriebsleistung anerkannt.</p>

  <div class="rule rule--sign"></div>
  <p class="issuer">Somnaris Schweiz AG<br>Quality Assurance</p>
</main>
</body>
</html>
```